Invitation to "movie night"
The Marlow Lane Picturehouse
Project: Invitation to "movie night"
Invitation to "movie night" - Personal
Creative Brief
We have an outdoor theater and need an invitation to send to our audience each week. Need to drop in details of each week's movie.
Personal
Personal friends and neighbors.
Email template or Word document -- customizable with information about this week's movie. "Movie starts at 8:30 p.m." "Bring a lawn chair, beach chair or blanket." Invitation from: Doreen & Frank Pellham. Address: 417 Marlow Lane, Natick, MA 01794. Telephone: 508-555-0183

```html
<!DOCTYPE html>
<html lang="en">
<head>
<meta charset="utf-8">
<title>The Marlow Lane Picturehouse – Movie Night</title>
<link rel="stylesheet" href="https://fonts.googleapis.com/css2?family=Bungee&family=Arimo:ital,wght@0,400;0,700;1,700&family=Poppins:ital,wght@1,800&family=Great+Vibes&family=Cormorant+Garamond:ital,wght@1,600&display=swap">
<style>
  :root {
    --ink-dark: #1c1c1c;
    --film-grey: #3a3a3a;
    --film-light: #6b6b6b;
    --lime: #b7e22a;
    --lime-soft: #a9d41f;
    --white: #ffffff;
    --pale: #e8e8e8;
    --gold: #f2e08a;
    --header-grey: #d6d6d6;
  }
  * { margin: 0; padding: 0; box-sizing: border-box; }
  html, body { width: 1200px; height: 972px; overflow: hidden; background: var(--ink-dark); }

  .invitation {
    position: relative;
    width: 1200px;
    height: 972px;
    overflow: hidden;
    background: linear-gradient(180deg, #2a2a2a 0%, #3d3d3d 45%, #2b2b2b 100%);
    font-family: "Arimo", Arial, sans-serif;
  }

  .countdown-leader {
    position: absolute;
    inset: 0;
    background:
      radial-gradient(circle at 330px 60px, rgba(120,120,120,.55) 0 150px, transparent 152px),
      radial-gradient(circle at 300px 480px, rgba(110,110,110,.45) 0 190px, transparent 192px),
      radial-gradient(circle at 900px 420px, rgba(100,100,100,.35) 0 200px, transparent 202px),
      linear-gradient(90deg, #2f2f2f 0%, #4a4a4a 30%, #3a3a3a 55%, #454545 75%, #2d2d2d 100%);
  }

  .film-bands { position: absolute; inset: 0; }

  .snacks-art {
    position: absolute;
    left: 60px; top: 10px;
    width: 480px; height: 300px;
    border-radius: 6px;
    background: linear-gradient(135deg, #e8c877 0%, #c9372c 45%, #f4efe4 70%, #3d3d3d 100%);
  }

  .masthead {
    position: absolute;
    left: 20px; top: 355px;
    width: 590px;
    text-align: center;
    color: var(--white);
    font-family: "Bungee", "Arial Black", sans-serif;
    font-weight: 400;
    line-height: 1.08;
    letter-spacing: 2px;
    text-shadow: 0 0 3px #000;
  }
  .masthead .line-small { font-size: 60px; }
  .masthead .line-main { font-size: 58px; }

  .presents {
    position: absolute;
    left: 0; top: 608px; width: 630px;
    text-align: center;
    font-family: "Great Vibes", cursive;
    font-size: 34px;
    color: var(--white);
  }

  .event-title {
    position: absolute;
    left: 0; top: 650px; width: 630px;
    text-align: center;
    font-family: "Poppins", sans-serif;
    font-style: italic;
    font-weight: 800;
    font-size: 76px;
    color: var(--lime);
    letter-spacing: 1px;
  }

  .host-invite {
    position: absolute;
    left: 160px; top: 815px;
    font-family: "Cormorant Garamond", serif;
    font-style: italic;
    font-weight: 600;
    color: var(--gold);
  }
  .host-invite .label { font-size: 50px; display: block; }
  .host-invite .hosts { font-size: 36px; display: block; margin-top: 4px; }

  .venue-bar {
    position: absolute;
    left: 640px; top: 0;
    width: 560px; height: 52px;
    background: #1e1e1e;
    color: var(--header-grey);
    font-weight: 700;
    font-size: 29px;
    letter-spacing: 1px;
    line-height: 52px;
    text-align: center;
    white-space: nowrap;
  }

  .tagline {
    position: absolute;
    left: 640px; top: 98px; width: 560px;
    text-align: center;
    color: var(--lime);
    font-weight: 700;
    font-size: 39px;
    line-height: 1.3;
  }

  .showtime {
    position: absolute;
    left: 650px; top: 318px; width: 550px;
    color: var(--white);
    text-align: center;
    white-space: nowrap;
  }
  .showtime .start { font-weight: 700; font-size: 35px; display: block; }
  .showtime .bring { font-weight: 700; font-size: 23px; display: block; margin-top: 14px; text-align: left; padding-left: 30px; color: var(--pale); }
  .showtime .sign { font-weight: 700; font-size: 23px; display: block; margin-top: 6px; text-align: left; padding-left: 80px; color: var(--pale); }

  .contact {
    position: absolute;
    left: 650px; top: 470px; width: 550px;
    color: var(--white);
    font-style: normal;
    font-weight: 700;
    white-space: nowrap;
  }
  .contact span { display: block; height: 44px; line-height: 44px; }
  .contact .heading { font-size: 29px; padding-left: 175px; }
  .contact .street { font-size: 28px; padding-left: 8px; }
  .contact .phone { font-size: 31px; padding-left: 22px; }

  .feature {
    position: absolute;
    left: 650px; top: 648px; width: 540px;
    color: var(--lime);
    text-align: center;
  }
  .feature h2 { font-size: 46px; font-weight: 700; line-height: 1; letter-spacing: .5px; }
  .feature p {
    margin-top: 10px;
    color: var(--lime-soft);
    font-size: 20px;
    line-height: 1.15;
    text-transform: uppercase;
  }
</style>
</head>
<body>
<main class="invitation">
  <div class="countdown-leader" role="img" aria-label="Film countdown leader with large faint numbers across a grey background"></div>

  <svg class="film-bands" width="1200" height="972" viewBox="0 0 1200 972" aria-hidden="true">
    <rect x="640" y="240" width="560" height="50" fill="#222" opacity=".55"/>
    <rect x="640" y="445" width="560" height="18" fill="#222" opacity=".5"/>
    <rect x="0" y="930" width="640" height="42" fill="#1f1f1f" opacity=".8"/>
    <line x1="632" y1="0" x2="632" y2="972" stroke="#1a1a1a" stroke-width="6"/>
  </svg>

  <div class="snacks-art" role="img" aria-label="Popcorn boxes, theatre masks and a film clapperboard"></div>

  <h1 class="masthead">
    <span class="line-small">THE</span><br>
    <span class="line-main">MARLOW LANE</span><br>
    <span class="line-main">PICTUREHOUSE</span>
  </h1>

  <div class="presents">Presents</div>
  <div class="event-title">MOVIE NIGHT</div>

  <div class="host-invite">
    <span class="label">Invitation from</span>
    <span class="hosts">Doreen &amp; Frank Pellham</span>
  </div>

  <div class="venue-bar">THE MARLOW LANE PICTUREHOUSE</div>

  <p class="tagline">Outdoor movies on the<br>banks of the Charles River</p>

  <div class="showtime">
    <span class="start">“MOVIE STARTS AT 8:30p.m.”</span>
    <span class="bring">“Bring a lawn chair, beach chair or blanket.”</span>
    <span class="sign">- Doreen &amp; Frank Pellham</span>
  </div>

  <address class="contact">
    <span class="heading">Address</span>
    <span class="street">417 Marlow Lane, Natick, MA 01794</span>
    <span class="phone">Telephone: 508-555-0183</span>
  </address>

  <section class="feature">
    <h2>THIS WEEKS MOVIE</h2>
    <p>This section can be customized to display info about the movie you will be showing each week. You can talk about the movie title and what the movie is about.</p>
  </section>
</main>
</body>
</html>
```